Sedona Themed Wedding Invitation & RSVP

*We have added our "Save the Date" for reference. We are not looking for an exact match, but we'd like the invitation and the "Save the Date" to coordinate. Our wedding colors are light pink, light green, cream, and gold. We have also added pictures of bouquets to give you an idea of the color palette and also examples of flowers and greenery to use in the invitation. What we like about the "Save the Date" is that it draws on the wedding colors and brings them in through the colors of the sunset.
*We have also added additional pictures the venue, the Le Verger Lodge, and several maps. We hope that you can use these to get a better feel for our venue and the theme of our wedding. It will be soft and romantic and at the very height of spring.
* We appreciated that many designers incorporated the Lodge at Le Vergre, we'd like to see more of that.
*Please note that we included some photos of Sedona for inspiration, please do not feel tied to these, do your own research and find what works best with your design.
*These maps are being included as references, but they are the work of other artists. Please make your own map from scratch and use these as references.
We would like a vertical quad-fold wedding invitation that has a perforated edge RSVP which can be sent as a postcard.
We have attached pictures of a similar style of invitation to serve as an example of the overall style we are looking for. We would like to see the end project be in a similar style of watercolor, but it would be Sedona themed throughout (rather than the forest theme presented in the attached example). We have also attached pictures of Sedona to serve as further inspiration. Below, we have provided an outline organized by panel (four panels on the front and four panels on the back) with descriptions of the more specific details:
-Front four panels:
-Panel 1: "Please join us for the wedding of Tobias and Colette"
-Panel 2: "Come out and celebrate. [INSERT TIME OF WEDDING HERE]
Saturday, May First 2021 at Le Verger de Rimoux"
-Panel 3: Custom map of Sedona. Include Le Verger de Rimoux on the
map (exemplar picture is of an idea for this is also included below)
- Panel 4: RSVP similar to one in the exemplar invitation. For RSVP date
deadline use April 1st, 2021. Address is 2287 W Marlow St Phoenix, AZ
85019
-Back four panels:
-Panel 1: Venue: Le Verger de Rimoux. 418 Fennick Ln, Sedona, AZ 86339.
Please arrive no earlier than XXX PM when valet services begin. Dinner
and dancing to follow the ceremony
-Panel 2: Hotels: Le Verger de Rimoux 418 Fennick Ln, Sedona, AZ 86339
(800) 612-3908; Bramwell Inn 917 N Tolliver Rd, Sedona, AZ 86339
(855) 238-6041.
"Hotel reservations can also be made through the links provided on our
website"
- Panel 3: "We have reserved a block of rooms for our guests. Please
mention the Pruett Halloway Wedding when you call to reserve."
"For additional details, please visit our wedding website and take a walk
down memory lane with us as we prepare to celebrate the rest of our
lives together: [INSERT WEDDING WEBSITE HERE AND
PASSWORD]"
- Panel 4: "Ceremony and celebration will be outdoors. Semi-formal attire
and flat shoes are recommended."
"Additionally, although we love your children, we want our wedding to
be your night off! Please know space is very limited; accordingly, we
encourage a weekend getaway for the grownups."
We'd like to have a succulent and rose at the bottom of the panel (an
exemplar picture is of an idea for this is also included below)
Updates
We have given extensive feedback to designers and would like to give them time to adjust their designs. Additionally, we have incorporated a lot more images into the brief that we hope will help!

```html
<!DOCTYPE html>
<html lang="en">
<head>
<meta charset="utf-8">
<title>Sedona Wedding Invitation – Tobias &amp; Colette</title>
<link rel="stylesheet" href="https://fonts.googleapis.com/css2?family=Great+Vibes&family=Cormorant+SC:wght@500;600&family=Oswald:wght@300;400&family=Courier+Prime&family=Dancing+Script:wght@500&display=swap">
<style>
  :root{
    --backdrop:#ebe6de;
    --paper:#efe5c8;
    --paper-edge:#e6d9b6;
    --plum:#5e1f47;
    --ink-soft:#6d5563;
    --fold:rgba(120,95,60,.18);
    --perf:#ffffff;
  }
  *{box-sizing:border-box;margin:0;padding:0}
  html,body{width:1013px;height:1200px;overflow:hidden;background:var(--backdrop)}
  body{position:relative;font-family:"Cormorant SC",serif;color:var(--plum)}

  .strip{position:absolute;top:128px;width:400px;box-shadow:0 6px 18px rgba(60,40,20,.18)}
  .strip--front{left:86px}
  .strip--back{left:527px}

  .panel{position:relative;height:236px;background:radial-gradient(ellipse at 50% 40%,var(--paper) 55%,var(--paper-edge) 100%);
    border-left:3px dotted var(--perf);border-right:3px dotted var(--perf);overflow:hidden;text-align:center}
  .panel + .panel{border-top:1px solid var(--fold)}
  .panel--rsvp{border-top:3px dotted var(--perf) !important}

  .script{font-family:"Great Vibes",cursive;font-weight:400}
  .caps{font-family:"Cormorant SC",serif;font-weight:600}
  .typed{font-family:"Courier Prime",monospace;color:var(--ink-soft)}

  /* front panel 1 */
  .title-kicker{position:absolute;top:6px;left:0;right:0;font-size:9px;letter-spacing:.5px}
  .title-the{position:absolute;top:18px;left:0;right:0;font-size:12px}
  .title-wedding{position:absolute;top:24px;left:0;right:0;font-size:32px;line-height:1.2}
  .title-of{position:absolute;top:62px;left:0;right:0;font-size:13px;color:#c07a3c}
  .art-rocks{position:absolute;left:0;right:0;top:62px;bottom:0;
    background:linear-gradient(180deg,rgba(239,229,200,0) 0%,#b8552a 22%,#8a3a1c 48%,#6e5a4a 72%,#8a7c6c 100%)}
  .names{position:absolute;left:0;right:0;top:100px;color:#f4efe6;line-height:1}
  .names .groom{display:block;font-size:54px;margin-left:-60px}
  .names .and{display:block;font-size:18px;margin:-10px 0 -6px -40px}
  .names .bride{display:block;font-size:54px;margin-left:70px}

  /* front panel 2 */
  .celebrate{position:absolute;top:8px;left:0;right:0;font-family:"Oswald",sans-serif;font-weight:300;font-size:15px;letter-spacing:.5px}
  .date-month{position:absolute;top:28px;left:0;right:0;font-size:24px;line-height:1.2}
  .date-day{position:absolute;top:56px;left:0;right:0;font-size:17px}
  .date-weekday{position:absolute;top:75px;left:0;right:0;font-size:7px}
  .date-time{position:absolute;top:85px;left:0;right:0;font-family:"Dancing Script",cursive;font-size:10px;color:#3a2230}
  .date-at{position:absolute;top:99px;left:0;right:0;font-size:9px}
  .date-venue{position:absolute;top:110px;left:0;right:0;font-size:9px}
  .art-butte{position:absolute;left:0;right:0;top:124px;bottom:0;
    background:radial-gradient(ellipse 70% 80% at 50% 45%,#5a60c8 0%,#8b7cc6 40%,rgba(190,170,160,.55) 75%,rgba(239,229,200,0) 100%),
               linear-gradient(180deg,rgba(239,229,200,0) 0%,rgba(170,185,175,.6) 100%)}

  /* front panel 3 */
  .art-map{position:absolute;inset:0;background:linear-gradient(90deg,#eee7cb 0%,#e3e6c0 45%,#a9d98a 100%)}

  /* front panel 4 — RSVP */
  .rsvp-by{position:absolute;top:10px;left:18px;width:170px;font-size:9px}
  .rsvp-date{position:absolute;top:32px;left:18px;width:170px;font-family:"Dancing Script",cursive;font-size:12px}
  .rsvp-date b{font-family:"Cormorant SC",serif;font-size:24px;font-weight:600;vertical-align:middle}
  .rsvp-date sup{font-size:8px}
  .rsvp-lines{position:absolute;top:74px;left:24px;width:168px;text-align:left}
  .rsvp-line{display:flex;align-items:flex-end;height:22px;font-family:"Oswald",sans-serif;font-size:13px}
  .rsvp-line span{flex:1;border-bottom:1px solid var(--plum);margin-left:8px;height:1px}
  .rsvp-line--blank span{margin-left:0}
  .rsvp-choices{position:absolute;top:138px;left:22px;text-align:left}
  .choice{display:flex;align-items:center;gap:7px;height:26px;font-family:"Oswald",sans-serif;font-size:13px}
  .choice i{display:inline-block;width:9px;height:9px;border:1px solid var(--plum)}
  .choice em{font-family:"Dancing Script",cursive;font-style:normal;font-size:13px}
  .rsvp-divider{position:absolute;left:236px;top:16px;bottom:12px;border-left:1px solid var(--plum)}
  .rsvp-address{position:absolute;left:236px;right:0;top:78px}
  .rsvp-address .to{font-size:13px;letter-spacing:.3px}
  .rsvp-address .line{font-size:9.5px;margin-top:2px}

  /* back panels */
  .heading{position:absolute;top:8px;left:18px;font-size:56px;line-height:1.35;font-weight:400}
  .venue-name{position:absolute;top:100px;left:0;right:0;font-size:10px}
  .venue-addr{position:absolute;top:114px;left:0;right:0;font-size:11px}
  .venue-note{position:absolute;top:160px;left:0;right:0;font-size:5.5px;line-height:1.3}
  .hotels{position:absolute;top:100px;left:0;right:0;font-size:9.5px;line-height:1.25}
  .hotels p + p{margin-top:9px}
  .hotels-note{position:absolute;top:204px;left:0;right:0;font-size:5.5px}
  .quote{font-size:9.5px;line-height:1.3}
  .typed-block{font-size:7px;line-height:1.75}
  .p-rooms .quote{position:absolute;top:34px;left:0;right:0}
  .p-rooms .typed-block{position:absolute;top:104px;left:0;right:0}
  .p-rooms .placeholder{position:absolute;top:180px;left:0;right:0;font-size:7px}
  .p-attire .quote{position:absolute;top:30px;left:0;right:0}
  .p-attire .typed-block{position:absolute;top:92px;left:0;right:0;font-size:7.5px;line-height:1.45}
  .art-flowers{position:absolute;left:125px;width:150px;bottom:10px;height:46px;border-radius:50%;
    background:radial-gradient(ellipse at 50% 50%,#c08ab0 0%,#e3a6b4 35%,#a9c8b4 70%,rgba(169,200,180,0) 100%)}
</style>
</head>
<body>

<section class="strip strip--front" aria-label="Invitation front">
  <div class="panel p-title">
    <div class="art-rocks" role="img" aria-label="Watercolor of Sedona red rock formations at sunset above desert scrub"></div>
    <div class="title-kicker caps">+ Please join us for +</div>
    <div class="title-the caps">The</div>
    <div class="title-wedding script">Wedding</div>
    <div class="title-of script">of</div>
    <div class="names script">
      <span class="groom">Tobias</span>
      <span class="and">and</span>
      <span class="bride">Colette</span>
    </div>
  </div>

  <div class="panel p-date">
    <div class="celebrate">× COME OUT &amp; CELEBRATE ×</div>
    <div class="date-month script">May</div>
    <div class="date-day caps">First ✻ 2021</div>
    <div class="date-weekday caps">Saturday</div>
    <div class="date-time">( Insert time of wedding here )</div>
    <div class="date-at script">at</div>
    <div class="date-venue caps">Le Verger de Rimoux</div>
    <div class="art-butte" role="img" aria-label="Watercolor of a Sedona butte in blue and red tones"></div>
  </div>

  <div class="panel p-map">
    <div class="art-map" role="img" aria-label="Illustrated map welcoming guests to Sedona, marking the venue Le Verger de Rimoux among nearby red rock landmarks, roads and the creek"></div>
  </div>

  <div class="panel panel--rsvp p-rsvp">
    <div class="rsvp-by caps">~ Please respond by ~</div>
    <div class="rsvp-date">✻ April <b>1<sup>st</sup></b> 2021 ✻</div>
    <div class="rsvp-lines">
      <div class="rsvp-line">M<span></span></div>
      <div class="rsvp-line rsvp-line--blank"><span></span></div>
    </div>
    <div class="rsvp-choices">
      <div class="choice"><i></i>YES! <em>so delighted to attend</em></div>
      <div class="choice"><i></i>NO! <em>regretfully decline</em></div>
    </div>
    <div class="rsvp-divider"></div>
    <div class="rsvp-address caps">
      <div class="to">Tobias and Colette</div>
      <div class="line">2287 W Marlow</div>
      <div class="line">St Phoenix, AZ 85019</div>
    </div>
  </div>
</section>

<section class="strip strip--back" aria-label="Invitation back">
  <div class="panel p-venue">
    <h2 class="heading script">Venue</h2>
    <div class="venue-name caps">Le Verger de Rimoux.</div>
    <div class="venue-addr caps">418 Fennick Ln, Sedona, AZ 86339</div>
    <div class="venue-note typed">Please arrive no earlier than XXX PM when valet services begin.<br>Dinner and dancing to follow the ceremony</div>
  </div>

  <div class="panel p-hotels">
    <h2 class="heading script">Hotels</h2>
    <div class="hotels caps">
      <p>Le Verger de Rimoux 418 Fennick Ln,<br>Sedona, AZ 86339<br>(800) 612-3908</p>
      <p>Bramwell Inn 917 N Tolliver Rd,<br>Sedona, AZ 86339<br>(855) 238-6041.</p>
    </div>
    <div class="hotels-note typed">"Hotel reservations can also be made through the links provided on our website"</div>
  </div>

  <div class="panel p-rooms">
    <p class="quote caps">"We have reserved a block of rooms for our guests.<br>Please mention the Pruett Halloway Wedding when you call to reserve."</p>
    <p class="typed-block typed">"For additional details,<br>please visit our wedding website and take<br>a walk down memory lane with us as we prepare to celebrate<br>the rest of our lives together:</p>
    <p class="placeholder typed">[INSERT WEDDING WEBSITE HERE AND PASSWORD]"</p>
  </div>

  <div class="panel p-attire">
    <p class="quote caps">"Ceremony and celebration will be outdoors.<br>Semi-formal attire and flat shoes are recommended."</p>
    <p class="typed-block typed">"Additionally, although we love your children,<br>we want our wedding to be your night off!<br>Please know space is very limited; accordingly,<br>we encourage a weekend getaway for the grownups."</p>
    <div class="art-flowers" role="img" aria-label="Watercolor spray of pink roses, a purple succulent and eucalyptus greenery"></div>
  </div>
</section>

</body>
</html>
```